IT Company Business Card design

Brisk Node is a new computer solutions business focusing on setting up servers and computer systems for small to medium sized businesses.

A business client will either request a solution, or support for a current system and we will turn up on site to provide these services.

We are bast in Christchurch, New Zealand.

We are looking for unique business card's that stand out and show off the business in a professional light.

Open to all idea's etc.

Industry/Entity Type

Computer

Requirements
Must have
• Business Logo (AI file attached)
Employee Name
Business title
Business landline number
Cell phone number
Email
Web URL
Nice to have
• Could be nice to have some keywords (possibly on the back) such as:

Business IT solutions
Network installations
Phone solutions
Server management
Software diagnostics

The above is not needed, just an idea.

```html
<!DOCTYPE html>
<html lang="en">
<head>
<meta charset="utf-8">
<title>Brisk Node – Business Card</title>
<link rel="stylesheet" href="https://fonts.googleapis.com/css2?family=Open+Sans:wght@300;400;600;700&display=swap">
<style>
  :root{
    --bg:#d9dadc;
    --navy:#14246b;
    --sky:#3f9fd8;
    --ink:#222428;
    --paper:#ffffff;
    --night:#0d0e10;
    --night-2:#1c1d21;
    --muted:#7e8590;
    --web:#7fc2e6;
  }
  *{margin:0;padding:0;box-sizing:border-box}
  html,body{width:1200px;height:871px;overflow:hidden}
  body{
    background:var(--bg);
    font-family:"Open Sans",Arial,sans-serif;
    display:flex;align-items:center;justify-content:center;gap:40px;
  }
  .card{
    position:relative;width:540px;height:309px;overflow:hidden;
    box-shadow:0 10px 30px rgba(0,0,0,.18);
  }
  .card__bands{position:absolute;inset:0;width:100%;height:100%}

  /* back side */
  .card--back{background:linear-gradient(135deg,var(--night-2),var(--night) 60%)}
  .back__brand{
    position:absolute;left:212px;top:42px;
    display:flex;align-items:center;gap:16px;
  }
  .brand-dot{width:38px;height:38px;border-radius:50%;background:var(--sky)}
  .brand-name{
    font-weight:300;font-size:30px;letter-spacing:.16em;text-transform:uppercase;
  }
  .back__brand .brand-name{color:#cfd3d8}
  .person{position:absolute;right:46px;top:128px;text-align:right;color:#e4e6e9}
  .person__name{font-weight:600;font-size:18px;letter-spacing:.01em}
  .person__role{font-weight:400;font-size:11px;color:#b9bdc4;margin-top:-2px}
  .contact{position:absolute;left:30px;color:var(--muted);font-size:11px;line-height:1.45}
  .contact--address{top:202px}
  .contact--phone{top:242px}
  .contact__row{display:flex;gap:10px;align-items:flex-start}
  .contact__icon{width:16px;height:16px;fill:var(--sky);margin-top:6px;flex:none}

  /* front side */
  .card--front{background:var(--paper)}
  .front__brand{
    position:absolute;left:0;right:0;top:124px;
    display:flex;align-items:center;justify-content:center;gap:18px;
  }
  .front__brand .brand-dot{width:52px;height:52px}
  .front__brand .brand-name{color:var(--ink);font-size:38px}
  .front__web{
    position:absolute;right:22px;top:262px;
    font-size:12px;color:var(--web);letter-spacing:.02em;
  }
</style>
</head>
<body>

  <section class="card card--back" aria-label="Business card, back">
    <svg class="card__bands" viewBox="0 0 540 309" aria-hidden="true">
      <rect x="316" y="172" width="224" height="14" fill="var(--navy)"/>
    </svg>
    <div class="back__brand">
      <span class="brand-dot"></span>
      <span class="brand-name">Brisk Node</span>
    </div>
    <div class="person">
      <div class="person__name">Mika HOLLOWAY</div>
      <div class="person__role">marketing manager</div>
    </div>
    <div class="contact contact--address">
      <div class="contact__row">
        <svg class="contact__icon" viewBox="0 0 16 16"><path d="M8 1 0 8h2v7h4v-4h4v4h4V8h2z"/></svg>
        <div>Harlow Street 14, Riccarton<br>Christchurch / NZ</div>
      </div>
    </div>
    <div class="contact contact--phone">
      <div class="contact__row">
        <svg class="contact__icon" viewBox="0 0 16 16"><path d="M3.6 1.2 6 3.6 4.6 5.6c.9 2 2.6 3.8 4.6 4.8L11 9l2.6 2.4-1.6 2.8C6.6 14 1.6 9 1.2 3.6z"/></svg>
        <div>+64 3 555 0142<br>+64 21 555 087</div>
      </div>
    </div>
  </section>

  <section class="card card--front" aria-label="Business card, front">
    <svg class="card__bands" viewBox="0 0 540 309" aria-hidden="true">
      <rect x="0" y="0" width="540" height="18" fill="var(--navy)"/>
      <rect x="0" y="238" width="540" height="4" fill="var(--sky)"/>
      <rect x="0" y="293" width="540" height="16" fill="var(--navy)"/>
    </svg>
    <div class="front__brand">
      <span class="brand-dot"></span>
      <span class="brand-name">Brisk Node</span>
    </div>
    <div class="front__web">www.brisknode.com</div>
  </section>

</body>
</html>
```